Design für Zeitungsanzeige hochwertige Betten
Zielgruppe
Ruhepunkt Sana verkauft hochwertige Bettsystem für schmerzfreies Liegen und Schlafen. Die Kunden (40+) kommen in das Geschäft, weil sie Rückenschmerzen haben und nicht gut schlafen können. Dort werden Sie individuell beraten. Ruhepunkt Sana hat einen Expertenstatus rum um das Thema Liegen und Schlafen, da Sie maßgeschneiderte Matratzen mit Hilfe von Liegedruckmessung anbieten. Die Produkte sind frei von Chemie und Pestiziden, was positiv zum guten Schlaf beiträgt. Somit sind die Produkte auch sehr hochwertig, aber auch kostspielig.
Aufgabenstellung
Gern einmal auf die Seite:
http://www.ruhepunkt-lindenau.de/traumbetten/
http://www.ruhepunkt-sana.com/betten/
-Vorher / nachher Bilder sind sehr effektvoll
-Unbedingt in die Anzeigen nehmen: Adresse- Logo Firma, "Ergonomische Betten" soll mit auf der Anzeige sein und vom Stil ähnlich zu der Schuhanzeige aufgebaut sein.
- gerne auch Unten mit GUTSCHEIN und einer Schere: Kostenlose Liegedruck-Messung
- Zielgruppe 40+
- ein Bett im Hintergrund würde sinnmachen, wenn eine Person davor steht und sich den Rücken hält.
- In der Art wollen wir auch die Anzeige haben. Gut wäre wenn eine ältere Dame zusehen ist, die genau der Zielgruppe entspricht.
Allgemeines:
- Die hohe Qualität der Produkte soll im Vordergrund stehen und die richtige Zielgruppe mit dem passenden Kleingeld ansprechen.
- Das Ruhepunkt Sana Logo muss zusehen sein und auffallen, da dieses sich bei den Menschen einprägen soll.
- Kunden sollen aufgefordert werden zu Ruhepunkt Sana ins Geschäft zu kommen und Ruhepunkt Sana als Experte und Berater soll im Vordergrund stehen.
- Adresse mit Ort muss zusehen sein.
Eine Zeitungsanzeige 4-farbig
Maße: querformat 5*9 cm (und vllt hochformat 4,5*14cm)

```html
<!DOCTYPE html>
<html lang="de">
<head>
<meta charset="utf-8">
<title>Ruhepunkt Sana – Ergonomische Betten</title>
<link href="https://fonts.googleapis.com/css2?family=Open+Sans:wght@400;600;700;800&family=Caveat:wght@600&display=swap" rel="stylesheet">
<style>
  :root {
    --green: #6aa93b;
    --green-light: #8cc063;
    --wine: #6b1e26;
    --wine-band: #7b232b;
    --ink: #1d1d1b;
    --paper: #ffffff;
    --frame: #9a9a9a;
    --photo-light: #eeeeec;
    --photo-mid: #d9d6d2;
    --photo-skin: #d8b8a6;
  }
  * { margin: 0; padding: 0; box-sizing: border-box; }
  html, body { width: 1200px; height: 667px; overflow: hidden; background: var(--paper); }
  .ad {
    position: relative;
    width: 1200px; height: 667px;
    background: var(--paper);
    border: 2px solid var(--frame);
    overflow: hidden;
    font-family: "Open Sans", Arial, sans-serif;
  }
  .hero-photo {
    position: absolute; left: 457px; top: 0; width: 743px; height: 359px;
    background:
      linear-gradient(90deg, var(--paper) 0%, rgba(255,255,255,0.6) 22%, rgba(255,255,255,0) 45%),
      radial-gradient(ellipse 38% 70% at 68% 60%, var(--photo-skin) 0%, rgba(216,184,166,0) 70%),
      linear-gradient(180deg, var(--photo-light) 0%, var(--photo-mid) 100%);
  }
  .category-band {
    position: absolute; right: 0; top: 0; width: 560px; height: 64px;
    background: linear-gradient(90deg, rgba(106,169,59,0) 0%, var(--green) 22%, var(--green) 100%);
    color: var(--paper);
    font-weight: 700; font-size: 33px; letter-spacing: 0.5px;
    display: flex; align-items: center; justify-content: flex-end;
    padding-right: 32px;
  }
  .headline {
    position: absolute; left: 64px; top: 52px;
    font-weight: 700; line-height: 1;
  }
  .headline .line { display: block; white-space: nowrap; }
  .headline .line-1 { font-size: 84px; letter-spacing: -1px; }
  .headline .line-1 .small { font-size: 62px; }
  .headline .line-2 { font-size: 90px; margin-top: 2px; letter-spacing: -1px; }
  .headline .line-3 { font-size: 66px; margin-top: 6px; }
  .green { color: var(--green); }
  .wine { color: var(--wine); }
  .cta-band {
    position: absolute; left: 0; top: 359px; width: 100%; height: 48px;
    background: linear-gradient(90deg, var(--wine-band) 0%, var(--wine-band) 70%, #8e3a40 100%);
    color: var(--paper);
    font-weight: 700; font-size: 27px;
    display: flex; align-items: center; padding-left: 64px;
  }
  .promise-badge {
    position: absolute; left: 916px; top: 115px; width: 244px; height: 244px;
    border-radius: 50%;
    background: var(--wine);
    color: var(--paper);
  }
  .promise-badge .inner {
    position: absolute; left: 34px; top: 34px;
    transform: rotate(-14deg); transform-origin: 60% 50%;
  }
  .promise-badge .motto {
    font-family: "Caveat", cursive;
    font-size: 34px; line-height: 0.95; text-align: center;
    width: 160px; margin-left: 10px;
  }
  .promise-badge ul { list-style: none; margin-top: 10px; }
  .promise-badge li {
    display: flex; align-items: center; gap: 8px;
    font-size: 23px; line-height: 1.25;
  }
  .promise-badge li svg { flex: none; }
  .brand-name {
    position: absolute; left: 64px; top: 470px;
    font-weight: 600; font-size: 86px; letter-spacing: -2px;
    color: var(--wine); line-height: 1;
  }
  .contact {
    position: absolute; right: 49px; top: 436px;
    text-align: right; color: var(--ink);
    font-size: 37px; line-height: 1.27;
  }
  .contact .phone {
    color: var(--wine); font-weight: 700; font-size: 35px; margin-top: 10px; letter-spacing: 1px;
  }
</style>
</head>
<body>
  <div class="ad">
    <div class="hero-photo" role="img" aria-label="Foto: Frau in hellem Nachthemd auf der Bettkante, die sich mit der Hand den schmerzenden Rücken hält"></div>

    <div class="category-band">ERGONOMISCHE BETTEN</div>

    <h1 class="headline">
      <span class="line line-1"><span class="green">Na,</span> <span class="green small">mal</span> <span class="wine">wieder</span></span>
      <span class="line line-2 wine">schlecht</span>
      <span class="line line-3 green">geschlafen?</span>
    </h1>

    <div class="promise-badge">
      <div class="inner">
        <p class="motto">Wir nehmen uns Zeit!</p>
        <ul>
          <li><svg width="20" height="20" viewBox="0 0 20 20"><circle cx="10" cy="10" r="10" fill="var(--green)"/><path d="M5 10.5l3.2 3.2L15 7" fill="none" stroke="#fff" stroke-width="2.6" stroke-linecap="round" stroke-linejoin="round"/></svg>Vorbeikommen</li>
          <li><svg width="20" height="20" viewBox="0 0 20 20"><circle cx="10" cy="10" r="10" fill="var(--green)"/><path d="M5 10.5l3.2 3.2L15 7" fill="none" stroke="#fff" stroke-width="2.6" stroke-linecap="round" stroke-linejoin="round"/></svg>Beraten lassen</li>
          <li><svg width="20" height="20" viewBox="0 0 20 20"><circle cx="10" cy="10" r="10" fill="var(--green)"/><path d="M5 10.5l3.2 3.2L15 7" fill="none" stroke="#fff" stroke-width="2.6" stroke-linecap="round" stroke-linejoin="round"/></svg>Probelaufen</li>
        </ul>
      </div>
    </div>

    <div class="cta-band">DANN KOMMEN SIE ZU UNS!</div>

    <div class="brand-name">Ruhepunkt Sana</div>

    <address class="contact" style="font-style: normal;">
      <div>Ruhepunkt Sana</div>
      <div>Lindenweg 7</div>
      <div>22941 Lindenau</div>
      <div class="phone">04107&nbsp; 38 52 19</div>
    </address>
  </div>
</body>
</html>
```